Traineeport.Asia, a social enterprise in Asia, needs a website!

I need a website designed for Traineeport.Asia, which is a social enterprise in Asia that connects potential interns with internship opportunities in the region.

Please read the attached wireframe and submit a homepage designs with text, based on the attached wireframe, from which we will choose and select the best design. Please note that we only want website designs; functionality, coding and programming are not required

The designer that provides the best designed home page, will then design all other pages of the website, and will receive the fee. We have already come up with one design (see wireframe in the attached doc) that designers may review for ideas.

Target Market(s)

University and graduate students in Asia.

Industry/Entity Type

Social

Number of Pages Required

5+ page

Font styles to use
Sans Serif

Requirements
Must have
• I want a website that doesn't require a significant amount of scrolling, and is well-designed so that it is easy to understand the website's purpose, how to navigate around the website, and utilize it.
Nice to have
• Easy to see all elements of the website without scrolling.

```html
<!DOCTYPE html>
<html lang="en">
<head>
<meta charset="utf-8">
<title>Traineeport.Asia</title>
<link rel="stylesheet" href="https://fonts.googleapis.com/css2?family=Open+Sans:wght@400;600&display=swap">
<style>
:root{
  --page:#ededed;
  --white:#ffffff;
  --green:#6cbd2c;
  --navy:#0f4da2;
  --navy-dark:#0b3f87;
  --text:#333333;
  --muted:#666666;
  --link:#2aa6d6;
  --line:#d4d4d4;
  --band:#e4ecf4;
  --band-grey:#e8e8e8;
  --summary:#e6f4fb;
  --footer:#bdbdbd;
}
*{box-sizing:border-box;margin:0;padding:0}
html,body{width:1081px;height:1200px;overflow:hidden}
body{background:var(--page);font-family:"Open Sans",Arial,sans-serif;color:var(--text);position:relative}
.site-header{position:absolute;left:133px;top:0;width:811px;height:87px}
.brand{position:absolute;left:8px;top:38px;font-size:20px;font-weight:600;color:var(--navy);display:flex;align-items:center;gap:8px}
.brand-dot{width:12px;height:12px;border-radius:50%;background:var(--green)}
.header-social{position:absolute;right:26px;top:32px;display:flex;gap:8px}
.header-social span{width:14px;height:14px;border-radius:50%;background:#b4b4b4}
.main-nav{position:absolute;left:133px;top:87px;width:811px;height:37px;display:flex;background:var(--navy)}
.main-nav a{display:flex;align-items:center;justify-content:center;color:#fff;font-size:12px;text-decoration:none;border-right:1px solid var(--navy-dark)}
.main-nav a.active{background:var(--green)}
.content{position:absolute;left:133px;top:124px;width:811px;height:1007px;background:var(--white)}
.panel{position:absolute;border:1px solid var(--line);background:#fff}
.hero{left:14px;top:20px;width:538px;height:300px;padding:3px}
.hero-image{position:absolute;inset:3px;background:linear-gradient(90deg,#7c7472 0%,#8e8785 45%,#b5aca4 70%,#8a7d70 100%)}
.hero-copy{position:absolute;left:22px;top:86px;width:240px;color:#fff}
.hero-copy h1{font-size:18px;font-weight:400;margin-bottom:10px}
.hero-copy p{font-size:14px;line-height:19px}
.section-head{height:37px;margin:3px;padding-left:8px;display:flex;align-items:center;font-size:16px;font-weight:600;text-transform:uppercase}
.featured{left:14px;top:335px;width:538px;height:298px}
.featured .section-head{background:var(--band)}
.jobs{display:grid;grid-template-columns:1fr 1fr;column-gap:16px;padding:6px 10px 0 12px}
.job{font-size:12px;line-height:18px;padding:8px 4px 7px;border-bottom:1px solid var(--line);height:66px}
.job.short{height:62px}
.job.last{border-bottom:none}
.more{position:absolute;right:26px;width:77px;height:19px;background:var(--navy);color:#fff;font-size:10px;display:flex;align-items:center;justify-content:center}
.featured .more{bottom:13px}
.resources{left:14px;top:647px;width:538px;height:337px}
.resources .section-head{background:var(--band-grey);padding-left:17px}
.resource{position:absolute;left:19px;top:78px;right:18px}
.resource-image{position:absolute;left:0;top:6px;width:127px;height:97px;background:linear-gradient(135deg,#2a3c55,#8ea6c2)}
.resource-body{margin-left:145px}
.resource-body h3{font-size:16px;font-weight:400;margin-bottom:10px}
.resource-body p{font-size:12px;line-height:18px;margin-bottom:9px}
.resources .more{bottom:14px}
.follow{position:absolute;left:562px;top:21px;width:241px;height:74px;background:var(--green);color:#fff;display:flex;align-items:center}
.follow-label{font-size:16px;padding:0 12px 0 18px;border-right:2px solid #fff;height:56px;display:flex;align-items:center}
.follow-icons{display:flex;gap:16px;padding-left:18px}
.follow-icons span{width:26px;height:26px;border-radius:50%;background:#fff}
.feed{left:562px;top:115px;width:241px;height:869px;padding:5px 6px}
.post{border:1px solid var(--line);height:138px;margin-bottom:6px;padding:11px 5px 0 12px;position:relative}
.post-thumb{position:absolute;left:12px;top:11px;width:53px;height:69px}
.post-info{margin-left:58px}
.post-info h4{font-size:13px;font-weight:400;margin-bottom:2px}
.post-info p{font-size:12px;line-height:15px;color:var(--muted);padding-left:3px}
.post-info p span{color:var(--link)}
.summary{position:absolute;left:12px;right:5px;bottom:10px;height:33px;background:var(--summary);display:flex;align-items:center;justify-content:center;gap:8px;font-size:13px}
.site-footer{position:absolute;left:0;top:1143px;width:1081px;height:57px;background:var(--footer);display:flex;align-items:center;justify-content:center;font-size:10px;color:#555}
</style>
</head>
<body>
<header class="site-header">
  <div class="brand"><span class="brand-dot"></span>Traineeport.Asia</div>
  <div class="header-social"><span></span><span></span></div>
</header>
<nav class="main-nav">
  <a class="active" style="width:108px">Home</a>
  <a style="width:120px">About Us</a>
  <a style="width:179px">Search Internships</a>
  <a style="width:104px">Login</a>
  <a style="width:139px">Registration</a>
  <a style="width:161px;border-right:none">For Employers</a>
</nav>
<main class="content">
  <section class="panel hero">
    <div class="hero-image" role="img" aria-label="Photo of a smiling student in a playful costume hat at a busy tech event"></div>
    <div class="hero-copy">
      <h1>Ready To Get Your Feet Wet?</h1>
      <p>Traineeport.Asia is apowerful network that helps talented students breaking through the professional world.</p>
    </div>
  </section>

  <section class="panel featured">
    <h2 class="section-head">Featured Jobs</h2>
    <div class="jobs">
      <p class="job">Lorem Ipsum is simply dummy text of the printing and typesetting industry. Lorem Ipsum has been the industry's.</p>
      <p class="job">Lorem Ipsum is simply dummy text of the printing and typesetting industry. Lorem Ipsum has been the industry's.</p>
      <p class="job short">Lorem Ipsum is simply dummy text of the printing and typesetting industry.</p>
      <p class="job short">Lorem Ipsum is simply dummy text of the printing and typesetting industry.</p>
      <p class="job last">Lorem Ipsum is simply dummy text of the printing and typesetting industry. Lorem Ipsum has been the industry's.</p>
      <p class="job last">Lorem Ipsum is simply dummy text of the printing and typesetting industry. Lorem Ipsum has been the industry's.</p>
    </div>
    <span class="more">read more..</span>
  </section>

  <section class="panel resources">
    <h2 class="section-head">Resources</h2>
    <article class="resource">
      <div class="resource-image" role="img" aria-label="Close-up photo of a hand typing on a keyboard"></div>
      <div class="resource-body">
        <h3>Resume / Cover Letter Tips</h3>
        <p>Lorem Ipsum is simply dummy text of the printing and typesetting industry. Lorem Ipsum has been the industry's. Standard dummy text ever since the when an unknown printer took a galley of type and scrambled it to make a type specimen book. It has survived not only five centuries,</p>
        <p>Lorem Ipsum is simply dummy text of the printing and typesetting industry. Lorem Ipsum has been the industry's. Standard dummy text ever since the when an unknown printer took a galley of type and scrambled.</p>
      </div>
    </article>
    <span class="more">read more..</span>
  </section>

  <aside class="follow">
    <span class="follow-label">Follow Us On</span>
    <div class="follow-icons"><span></span><span></span></div>
  </aside>

  <section class="panel feed">
    <article class="post">
      <div class="post-thumb" role="img" aria-label="Publisher avatar" style="background:#111"></div>
      <div class="post-info"><h4>Pressline @ Pressline - 23m</h4><p>Lorem Ipsum is simply dummy text of the <span>typesetting industry.</span></p></div>
      <div class="summary"><svg width="12" height="14" viewBox="0 0 12 14"><path d="M1 1h7l3 3v9H1z" fill="none" stroke="#333"/></svg>View Summary</div>
    </article>
    <article class="post">
      <div class="post-thumb" role="img" aria-label="Gaming league avatar" style="background:linear-gradient(135deg,#1c2a4a,#5a4a8a)"></div>
      <div class="post-info"><h4>Pressline @ Pressline - 23m</h4><p>Lorem Ipsum is simply dummy text of the <span>typesetting industry.</span></p></div>
      <div class="summary"><svg width="12" height="14" viewBox="0 0 12 14"><path d="M1 1h7l3 3v9H1z" fill="none" stroke="#333"/></svg>View Summary</div>
    </article>
    <article class="post">
      <div class="post-thumb" role="img" aria-label="Photo of a campus building" style="background:linear-gradient(180deg,#6fa3d8,#b26a4e)"></div>
      <div class="post-info"><h4>Pressline @ Pressline - 23m</h4><p>Lorem Ipsum is simply dummy text of the <span>typesetting industry.</span></p></div>
      <div class="summary"><svg width="12" height="14" viewBox="0 0 12 14"><path d="M1 1h7l3 3v9H1z" fill="none" stroke="#333"/></svg>View Summary</div>
    </article>
    <article class="post">
      <div class="post-thumb" role="img" aria-label="Company avatar" style="background:#1f5c99"></div>
      <div class="post-info"><h4>Pressline @ Pressline - 23m</h4><p>Lorem Ipsum is simply dummy text of the <span>typesetting industry.</span></p></div>
      <div class="summary"><svg width="12" height="14" viewBox="0 0 12 14"><path d="M1 1h7l3 3v9H1z" fill="none" stroke="#333"/></svg>View Summary</div>
    </article>
    <article class="post">
      <div class="post-thumb" role="img" aria-label="Photo of a campus building" style="background:linear-gradient(180deg,#6fa3d8,#b26a4e)"></div>
      <div class="post-info"><h4>Pressline @ Pressline - 23m</h4><p>Lorem Ipsum is simply dummy text of the <span>typesetting industry.</span></p></div>
      <div class="summary"><svg width="12" height="14" viewBox="0 0 12 14"><path d="M1 1h7l3 3v9H1z" fill="none" stroke="#333"/></svg>View Summary</div>
    </article>
    <article class="post" style="margin-bottom:0">
      <div class="post-thumb" role="img" aria-label="Company avatar" style="background:#1f5c99"></div>
      <div class="post-info"><h4>Pressline @ Pressline - 23m</h4><p>Lorem Ipsum is simply dummy text of the <span>typesetting industry.</span></p></div>
      <div class="summary"><svg width="12" height="14" viewBox="0 0 12 14"><path d="M1 1h7l3 3v9H1z" fill="none" stroke="#333"/></svg>View Summary</div>
    </article>
  </section>
</main>
<footer class="site-footer">© 2015 All rights resesrved.</footer>
</body>
</html>
```